Volora Laundry and Dry Cleaning Poster

We need a Poster and Window Sticker for our Laundry and Dry cleaning shop (VOLORA LAUNDRY AND DRY CLEANING).
info we like on the design. Logo is included
Company Name: Volora Laundry and Dry Cleaning
Slogan: It Comes Back Clean
Location: Kwentu-Dasor, Accra
Working Hours: Mon-Sat 8am to 5pm
Tel: +233 30 781 6242
email:info@voloralaundry.example
website: www.voloralaundry.example
fb: fb.com/voloralaundry

Target Market(s)

Laundry Shop

Colors
33a6d7
9bcb3b

```html
<!DOCTYPE html>
<html lang="en">
<head>
<meta charset="utf-8">
<title>Volora Laundry and Dry Cleaning Poster</title>
<link rel="stylesheet" href="https://fonts.googleapis.com/css2?family=Montserrat:wght@600;700;800&display=swap">
<style>
  :root {
    --page-bg: #eceeef;
    --brand-blue: #33a6d7;
    --brand-blue-light: #5cc0ea;
    --brand-blue-deep: #1f6fb0;
    --brand-green: #3aa63a;
    --logo-green: #2e9a4a;
    --white: #ffffff;
    --pill-shadow: rgba(0, 40, 80, 0.25);
  }
  * { box-sizing: border-box; margin: 0; padding: 0; }
  html, body {
    width: 1200px; height: 1000px; overflow: hidden;
    background: var(--page-bg);
    font-family: "Montserrat", Arial, sans-serif;
  }
  .poster {
    position: absolute; left: 264px; top: 20px;
    width: 671px; height: 960px;
    background: linear-gradient(180deg, #3db0e4 0%, var(--brand-blue) 45%, var(--brand-blue-light) 100%);
    overflow: hidden;
  }
  .headline {
    position: absolute; top: 30px; left: 0; width: 100%;
    text-align: center; color: var(--white);
  }
  .headline__name {
    font-weight: 700; font-size: 45px; line-height: 52px; letter-spacing: 0.5px;
  }
  .headline__rule {
    width: 440px; height: 1px; margin: 6px auto 6px;
    background: rgba(255,255,255,0.75);
  }
  .headline__slogan {
    font-weight: 700; font-size: 30px; line-height: 34px; letter-spacing: 0.5px;
  }
  .pill {
    position: absolute; height: 44px; border-radius: 22px;
    background: var(--white);
    box-shadow: 0 4px 8px var(--pill-shadow);
    display: flex; align-items: center; justify-content: center;
    font-weight: 700; font-size: 22px; font-variant: small-caps;
    color: var(--brand-green);
    white-space: nowrap;
  }
  .pill--location { left: 102px; top: 216px; width: 473px; }
  .pill--hours { left: 83px; top: 281px; width: 510px; }
  .pill--phone {
    left: 160px; top: 346px; width: 357px;
    color: var(--brand-blue-deep); font-variant: normal; font-size: 23px;
  }
  .hero-art {
    position: absolute; left: 12px; top: 400px; width: 660px; height: 450px;
    background: radial-gradient(ellipse at 45% 55%, #f3f6fa 0%, #d5e6f3 35%, rgba(120,190,230,0.6) 60%, rgba(51,166,215,0) 78%);
  }
  .contacts {
    position: absolute; left: 34px; top: 862px;
    list-style: none; color: var(--white);
    font-weight: 600; font-size: 20px; line-height: 30px;
  }
  .contacts__item { display: flex; align-items: center; gap: 8px; }
  .contacts__icon { width: 18px; height: 18px; flex: none; }
  .brand-corner {
    position: absolute; left: 405px; top: 858px; width: 266px; height: 102px;
    background: var(--white);
    border-top-left-radius: 70px;
    display: flex; align-items: center; justify-content: center; gap: 10px;
  }
  .brand-corner__dot {
    width: 42px; height: 42px; border-radius: 50%;
    background: var(--brand-blue); flex: none;
  }
  .brand-corner__name {
    color: var(--logo-green); font-weight: 700; font-size: 17px; line-height: 20px;
    width: 150px;
  }
</style>
</head>
<body>
  <main class="poster">
    <header class="headline">
      <h1 class="headline__name">VOLORA LAUNDRY<br>AND DRY CLEANING</h1>
      <div class="headline__rule"></div>
      <p class="headline__slogan">IT COMES BACK CLEAN</p>
    </header>

    <div class="pill pill--location">Location : Kwentu-Dasor, Accra</div>
    <div class="pill pill--hours">Working Hours: Mon-Sat 8am to 5pm</div>
    <div class="pill pill--phone">Call +233 30 781 6242</div>

    <div class="hero-art" role="img" aria-label="Stack of folded clean white shirts with a water splash and soap bubbles"></div>

    <ul class="contacts">
      <li class="contacts__item">
        <svg class="contacts__icon" viewBox="0 0 18 18" aria-hidden="true">
          <rect x="1" y="3" width="16" height="12" rx="2" fill="none" stroke="#fff" stroke-width="1.8"/>
          <path d="M2 4.5 L9 10 L16 4.5" fill="none" stroke="#fff" stroke-width="1.8"/>
        </svg>
        info@voloralaundry.example
      </li>
      <li class="contacts__item">
        <svg class="contacts__icon" viewBox="0 0 18 18" aria-hidden="true">
          <circle cx="9" cy="9" r="7.5" fill="none" stroke="#fff" stroke-width="1.6"/>
          <ellipse cx="9" cy="9" rx="3.2" ry="7.5" fill="none" stroke="#fff" stroke-width="1.4"/>
          <path d="M1.5 9 H16.5" stroke="#fff" stroke-width="1.4"/>
        </svg>
        www.voloralaundry.example
      </li>
      <li class="contacts__item">
        <svg class="contacts__icon" viewBox="0 0 18 18" aria-hidden="true">
          <circle cx="9" cy="9" r="8" fill="#fff"/>
        </svg>
        voloralaundry
      </li>
    </ul>

    <div class="brand-corner">
      <span class="brand-corner__dot"></span>
      <span class="brand-corner__name">Volora Laundry and Dry Cleaning</span>
    </div>
  </main>
</body>
</html>
```